Masonry and Landscaping Construction company business card

Looking for a business card design for a construction company named Ferrano Construction. It is an italian-american family business that specializes in custom stone work, patios, walkways, driveways, steps, outdoor kitchens, concrete, waterproofing, power wash, landscaping and more. Our colors are mostly red and white with some black. We're looking for a bold design. we also like to incorporate a picture of my family's hometown somewhere in it.
Target Market(s)
Luxury home owners
Industry/Entity Type
Construction
Contact Information for Business Card
Details includes should be bullet points mentioning the services provided. Custom Stone Work, Outdoor Kitchens, Fire Pits, Patios, Walkways, Steps, Concrete, Waterproofing, powerwash and landscaping
Requirements
Must have
- Would like a spot on the card for co-owners names, numbers and email to be listed also looking to add the QR code for an instagram page
Nice to have
- would like something bold, based around the colors red and white with black outlines or details

```html
<!DOCTYPE html>
<html lang="en">
<head>
<meta charset="utf-8">
<title>Ferrano Construction – Business Card</title>
<link href="https://fonts.googleapis.com/css2?family=Montserrat:wght@500;700;800&family=Oswald:wght@300;400;500&display=swap" rel="stylesheet">
<style>
  :root {
    --page-bg: #e9e9e9;
    --card-bg: #ffffff;
    --brand-red: #e3232b;
    --ink: #2b2b2b;
    --ink-soft: #444444;
    --muted: #3a3a3a;
  }
  * { box-sizing: border-box; margin: 0; padding: 0; }
  html, body {
    width: 965px; height: 1200px; overflow: hidden;
    background: var(--page-bg);
    font-family: "Montserrat", Arial, sans-serif;
  }
  .canvas { position: relative; width: 965px; height: 1200px; }

  .card {
    position: absolute; left: 70px; width: 790px;
    border-radius: 24px; overflow: hidden;
    background: var(--card-bg);
    box-shadow: 0 10px 28px rgba(0,0,0,0.12);
  }
  .card--front { top: 129px; height: 460px; }
  .card--back  { top: 628px; height: 451px; }

  /* Brand name (stands where the mark sits) */
  .brand-name {
    position: absolute; display: flex; align-items: center; gap: 14px;
    font-family: "Montserrat", Arial, sans-serif; font-weight: 800;
    color: var(--ink); text-transform: uppercase; line-height: 1.05;
  }
  .brand-name__mark { flex: none; border-radius: 50%; background: var(--brand-red); }
  .card--front .brand-name { left: 70px; top: 196px; width: 300px; font-size: 31px; }
  .card--front .brand-name__mark { width: 30px; height: 30px; }

  .divider {
    position: absolute; left: 386px; top: 103px;
    width: 2px; height: 273px; background: var(--brand-red);
  }
  .contact { position: absolute; left: 411px; top: 94px; color: var(--ink-soft); }
  .contact__name { font-size: 30px; font-weight: 800; color: var(--brand-red); line-height: 1.2; }
  .contact__role { font-size: 20px; font-weight: 500; margin-top: 4px; }
  .contact__list { list-style: none; margin-top: 24px; }
  .contact__item {
    display: flex; align-items: center; gap: 18px;
    font-size: 21px; font-weight: 500; height: 33px;
  }
  .contact__icon { width: 22px; height: 22px; flex: none; }
  .contact__address { margin-top: 20px; margin-left: 8px; font-size: 21px; font-weight: 500; line-height: 34px; }

  /* Back */
  .hometown-photo {
    position: absolute; inset: 0;
    background:
      linear-gradient(180deg, rgba(255,255,255,0.35) 0%, rgba(255,255,255,0.5) 100%),
      linear-gradient(180deg, #e4e8e6 0%, #c9d3c6 22%, #a9b9a0 42%, #b7bfae 58%, #cfc5b8 76%, #c4ccb6 100%);
  }
  .card--back .brand-name {
    left: 0; right: 0; top: 108px; justify-content: center;
    font-size: 44px; text-align: left;
  }
  .card--back .brand-name__mark { width: 40px; height: 40px; }
  .services { position: absolute; left: 0; right: 0; top: 315px; text-align: center; }
  .services__title {
    font-family: "Oswald", Arial, sans-serif; font-weight: 500;
    font-size: 25px; letter-spacing: 8px; color: var(--brand-red);
  }
  .services__list {
    margin-top: 12px;
    font-family: "Oswald", Arial, sans-serif; font-weight: 300;
    font-size: 27px; line-height: 31px; color: var(--muted);
    white-space: nowrap;
  }
</style>
</head>
<body>
<main class="canvas">

  <section class="card card--front">
    <div class="brand-name"><span class="brand-name__mark"></span><span>Ferrano<br>Construction</span></div>
    <div class="divider"></div>
    <div class="contact">
      <p class="contact__name">John Smith</p>
      <p class="contact__role">Owner</p>
      <ul class="contact__list">
        <li class="contact__item">
          <svg class="contact__icon" viewBox="0 0 24 24"><path fill="#e3232b" d="M6.6 10.8a15.1 15.1 0 0 0 6.6 6.6l2.2-2.2c.3-.3.7-.4 1-.2 1.1.4 2.3.6 3.6.6.6 0 1 .4 1 1V20c0 .6-.4 1-1 1A17 17 0 0 1 3 4c0-.6.4-1 1-1h3.5c.6 0 1 .4 1 1 0 1.3.2 2.5.6 3.6.1.3 0 .7-.2 1z"/></svg>
          <span>123-456-7890</span>
        </li>
        <li class="contact__item">
          <svg class="contact__icon" viewBox="0 0 24 24"><rect x="1" y="5" width="22" height="15" fill="#e3232b"/><path d="M1 5l11 8 11-8" fill="none" stroke="#fff" stroke-width="2"/></svg>
          <span>info@webname.com</span>
        </li>
        <li class="contact__item">
          <svg class="contact__icon" viewBox="0 0 24 24"><circle cx="12" cy="12" r="11" fill="#e3232b"/><path d="M7 6c2 1 3 3 2 5s1 3 2 4-1 4-1 6M15 3c0 2 2 3 4 3M14 13c2-1 4 0 5 2" fill="none" stroke="#fff" stroke-width="1.6"/></svg>
          <span>www.websitename.com</span>
        </li>
      </ul>
      <p class="contact__address">448 address line here<br>45452, Country Name</p>
    </div>
  </section>

  <section class="card card--back">
    <div class="hometown-photo" role="img" aria-label="Faded photo of the family's Italian hometown: bell tower, stone houses and green hills"></div>
    <div class="brand-name"><span class="brand-name__mark"></span><span>Ferrano<br>Construction</span></div>
    <div class="services">
      <h2 class="services__title">OUR SERVICES</h2>
      <p class="services__list">
        • Custom Stone Work &nbsp;• Outdoor Kitchens &nbsp;• Fire Pits &nbsp;• Patios &nbsp;• Steps<br>
        • Walkways &nbsp;&nbsp;• Concrete &nbsp;• Waterproofing &nbsp;• Powerwash and landscaping
      </p>
    </div>
  </section>

</main>
</body>
</html>
```